Brightvale, The Pixel Nest or Coding for Kids

Brightvale
We build talent
We need a creative inspiring poster design for a new company based in Bahrain called 'Brightvale'. we teach children computer coding (game developments) and robotics in a play like environment. (activity-based not lectured based) which will develop kids talents in a challenging and enjoying way. (serious and fun)

we like and eye catching poster that will inspire kids to join our academy. Use vibrant color to create energy, elicit a mood and attract the eye.
The poster should be based on our value of:
Inspiration
learning is fun
knowledge is power

Relevant ideas were written on the image I attached.
Updates

Target Market(s)

Parents and KIds

Industry/Entity Type

Education

Logo Text

Brightvale, Building Talents

Font styles to use
Sans Serif

Colors
ec1f27
f37122
f78f20
ffc214
fbef40
9bcb3c
add136
33b8a4
33a6d7

Requirements
Must have
• looking for a design that when a parent see it: "I want to get my kid in to coding!"
• attractive,elegant,colorful,inspiring with a simple and strong message.

```html
<!DOCTYPE html>
<html lang="en">
<head>
<meta charset="utf-8">
<title>Brightvale – The Pixel Nest</title>
<link rel="stylesheet" href="https://fonts.googleapis.com/css2?family=Arimo:ital,wght@0,700;1,700&display=swap">
<style>
  :root {
    --lime: #d5df22;
    --ink: #231f20;
    --screen-teal: #2fb1a6;
    --screen-teal-deep: #279d94;
    --white: #ffffff;
  }
  html, body {
    margin: 0;
    padding: 0;
    width: 1200px;
    height: 1005px;
    overflow: hidden;
    background: var(--lime);
  }
  .poster {
    display: block;
    width: 1200px;
    height: 1005px;
  }
  .tablet-body { fill: var(--ink); }
  .tablet-button { fill: var(--white); }
  .screen-frame { fill: none; stroke: var(--white); stroke-width: 3; }
  .brand-name,
  .club-name {
    font-family: "Arimo", Arial, sans-serif;
    font-weight: 700;
    fill: var(--ink);
  }
  .brand-name { font-size: 96px; }
  .club-name { font-size: 44px; }
  .web-address,
  .tagline {
    font-family: "Arimo", Arial, sans-serif;
    font-weight: 700;
    font-style: italic;
    font-size: 53px;
    fill: var(--ink);
  }
</style>
</head>
<body>
<svg class="poster" viewBox="0 0 1200 1005" xmlns="http://www.w3.org/2000/svg">
  <defs>
    <linearGradient id="screen-fill" x1="0" y1="0" x2="1" y2="1">
      <stop offset="0" stop-color="var(--screen-teal)"/>
      <stop offset="1" stop-color="var(--screen-teal-deep)"/>
    </linearGradient>
  </defs>

  <g class="tablet">
    <rect class="tablet-body" x="125" y="103" width="931" height="621" rx="27"/>
    <circle class="tablet-button" cx="171" cy="417" r="21"/>
    <rect class="screen-area" x="220" y="157" width="777" height="512" rx="14"
          fill="url(#screen-fill)" role="img"
          aria-label="Screen filled with rows of binary code digits"/>
    <rect class="screen-frame" x="220" y="157" width="777" height="512" rx="14"/>
  </g>

  <g class="screen-title">
    <text class="brand-name" x="608" y="410" text-anchor="middle">BRIGHTVALE</text>
    <text class="club-name" x="608" y="478" text-anchor="middle">The Pixel Nest</text>
  </g>

  <text class="web-address" x="590" y="829" text-anchor="middle">www.brightvale-kids.com</text>
  <text class="tagline" x="590" y="907" text-anchor="middle"
        textLength="669" lengthAdjust="spacingAndGlyphs">where kids learn to code</text>
</svg>
</body>
</html>
```